Internal Web Pages for Metricsy Hub

I need internal web pages (Why Metricsy Hub?, What We Offer, Blog, Testimonials) that match the design of the homepage. These do not need to be as long or in-depth as the landing page (provided for reference) but I will need three, maybe four, total pages (I'll select the max number of pages for now, but these will all be simple and short pages). Also attached is our new logo design for the company.

They are to essentially be:
Why Metricsy Hub? - An About Us and Why Choose Us page rolled into one.
What We Offer - A Services type page
Blog - self-explanatory
Testimonials - Customer Reviews and Use Cases

Also, maybe a very simple "Contact Us" page as well.

Target Market(s)

Business professionals that work with data analytics teams

Industry/Entity Type

Data Science

Number of Pages Required

5+ page

Requirements
Must have
• It must match the original design in theme and colors.
Nice to have
• Simple pages that show continuity that flows from the original landing page.
Should not have
• Can not be a different design that does not match the landing page.

```html
<!DOCTYPE html>
<html lang="en">
<head>
<meta charset="utf-8">
<title>Metricsy Hub – Internal Pages</title>
<link href="https://fonts.googleapis.com/css2?family=Oswald:wght@600;700&family=Poppins:wght@300;400;500;600&display=swap" rel="stylesheet">
<style>
:root{
  --bg:#2a1a55;
  --bg-soft:#3a2a6c;
  --bg-softer:#46367a;
  --footer:#200e55;
  --footer-bar:#1a0a47;
  --hero-a:#1b1240;
  --hero-b:#3b2f7a;
  --accent:#4f5ce0;
  --accent-soft:#e9ebfb;
  --orange:#f28a1a;
  --ink:#2f2f3a;
  --muted:#8a8a96;
  --line:#e6e6ee;
  --white:#ffffff;
}
*{box-sizing:border-box;margin:0;padding:0}
html,body{width:1200px;height:2979px;overflow:hidden}
body{background:var(--bg);font-family:'Poppins',sans-serif;color:var(--ink);position:relative}
.backdrop{position:absolute;inset:0;width:1200px;height:2979px}
.brand{position:absolute;top:100px;left:0;width:1200px;display:flex;justify-content:center;align-items:center;gap:26px}
.brand-mark{width:92px;height:92px;border-radius:50%;background:var(--accent)}
.brand-name{font-family:'Poppins',sans-serif;font-weight:300;font-size:96px;color:var(--white);letter-spacing:1px;line-height:1}
.section-title{position:absolute;font-family:'Oswald',sans-serif;font-weight:700;font-size:36px;color:var(--white);letter-spacing:.3px;line-height:1}
.page{position:absolute;width:388px;background:var(--white);overflow:hidden;box-shadow:0 14px 30px rgba(0,0,0,.35)}
.nav{position:absolute;top:0;left:0;right:0;height:28px;background:var(--white);display:flex;align-items:center;padding:0 30px}
.nav-logo{display:flex;align-items:center;gap:4px;font-size:11px;font-weight:400;color:var(--ink)}
.nav-logo i{display:block;width:14px;height:10px;background:var(--accent)}
.nav-links{display:flex;gap:11px;margin-left:16px;font-size:5.5px;color:var(--muted)}
.nav-links .on{color:var(--accent)}
.nav-cta{margin-left:auto;background:var(--orange);color:var(--white);font-size:4.2px;font-weight:600;padding:3px 6px}
.hero{position:absolute;top:28px;left:0;width:388px;height:130px;background:linear-gradient(110deg,var(--hero-a),var(--hero-b));clip-path:polygon(0 0,100% 0,100% 72%,48% 100%,0 66%)}
.hero-edge{position:absolute;top:28px;left:0;width:388px;height:132px}
.hero-title{position:absolute;left:27px;top:72px;color:var(--white);font-size:12px;font-weight:400}
.crumb{position:absolute;left:27px;top:91px;color:var(--white);font-size:4.6px;display:flex;gap:3px;align-items:center}
.crumb b{display:inline-block;width:4px;height:4px;background:var(--orange);border-radius:1px}
.heading{position:absolute;left:0;right:0;text-align:center;font-size:11.5px;font-weight:400;color:var(--ink)}
.heading::after{content:"";display:block;width:34px;height:1px;background:var(--line);margin:6px auto 0}
.body{font-size:4.4px;line-height:1.55;color:var(--muted)}
.footer{position:absolute;left:0;right:0;bottom:0;background:var(--footer);color:#cfcbe6}
.footer-main{position:relative;height:127px}
.footer-bar{height:46px;background:var(--footer-bar);font-size:4.3px;color:#d8d4ef;text-align:center;padding-top:22px}
.f-logo{position:absolute;left:46px;top:22px;display:flex;align-items:center;gap:4px;font-size:11px;color:var(--white)}
.f-logo i{display:block;width:14px;height:10px;background:var(--accent)}
.f-desc{position:absolute;left:46px;top:40px;width:92px;font-size:4.2px;line-height:1.5;color:#bcb6dc}
.f-social{position:absolute;left:46px;top:83px;display:flex;gap:3px}
.f-social span{width:9px;height:9px;border:0.8px solid #cfcbe6;border-radius:50%}
.f-col-h{position:absolute;top:22px;font-size:5px;font-weight:600;color:var(--white)}
.f-contact{position:absolute;left:155px;top:36px;font-size:4.4px;line-height:1.5;color:var(--white)}
.f-contact p{position:relative;padding-left:12px;margin-bottom:4px;font-weight:500}
.f-contact svg{position:absolute;left:0;top:1px;width:7px;height:7px}
.f-sign{position:absolute;left:244px;top:36px;width:98px;font-size:4.2px;line-height:1.5;color:#bcb6dc}
.f-input{margin-top:5px;height:11px;background:var(--white);font-size:3.8px;color:var(--muted);padding:3px 5px}
.f-btn{display:inline-block;margin-top:5px;background:var(--orange);color:var(--white);font-size:3.8px;font-weight:600;padding:3px 7px}
.card{position:absolute;background:var(--white);box-shadow:0 2px 8px rgba(40,30,90,.12)}
.card h4{font-size:5px;font-weight:600;color:var(--ink);margin-bottom:4px}
.photo{position:absolute}
.stars{color:var(--orange);font-size:4.5px;letter-spacing:.5px}
.avatar{display:inline-block;width:11px;height:11px;border-radius:50%;background:#c7c2d8;vertical-align:middle}
.person{position:absolute;font-size:4.2px;line-height:1.3;color:var(--ink);display:flex;gap:4px;align-items:center}
.person small{display:block;font-size:3.6px;color:var(--muted)}
.dot{position:absolute;width:8px;height:8px;border-radius:50%;background:var(--accent)}
.icon-bubble{position:absolute;width:40px;height:26px;border-radius:13px;background:#f1f1f6}
.icon-box{position:absolute;width:22px;height:22px}
</style>
</head>
<body>

<svg class="backdrop" viewBox="0 0 1200 2979" aria-hidden="true">
  <path d="M0 1090 C 200 860, 420 760, 640 640 S 1050 420, 1200 380 L1200 2979 L0 2979 Z" fill="var(--bg-soft)"/>
  <path d="M0 2140 C 300 1960, 600 1900, 900 1780 S 1150 1700, 1200 1690 L1200 2979 L0 2979 Z" fill="var(--bg-softer)" opacity=".55"/>
  <path d="M0 2600 C 400 2460, 800 2500, 1200 2380 L1200 2979 L0 2979 Z" fill="var(--bg)" opacity=".5"/>
</svg>

<header class="brand">
  <div class="brand-mark"></div>
  <div class="brand-name">Metricsy Hub</div>
</header>

<!-- WHY -->
<h2 class="section-title" style="left:196px;top:306px">WHY METRICSY HUB</h2>
<section class="page" style="left:197px;top:361px;height:789px">
  <nav class="nav"><div class="nav-logo"><i></i>Metricsy Hub</div><div class="nav-links"><span>Home</span><span class="on">About us</span><span>Our Service</span><span>Blog</span><span>Contact</span></div><div class="nav-cta">GET STARTED</div></nav>
  <div class="hero" role="img" aria-label="Hero photo of a person using a glowing data dashboard interface"></div>
  <svg class="hero-edge" viewBox="0 0 388 132" aria-hidden="true"><polyline points="80,110 186,130 388,95" fill="none" stroke="var(--accent)" stroke-width="2"/></svg>
  <div class="hero-title">Why Metricsy Hub?</div>
  <div class="crumb"><b></b>Home | Why Metricsy Hub?</div>

  <div style="position:absolute;left:47px;top:190px;font-size:10.5px">About Metricsy Hub</div>
  <div style="position:absolute;left:47px;top:203px;width:24px;height:1px;background:var(--line)"></div>
  <p class="body" style="position:absolute;left:47px;top:218px;width:138px">Sed ut perspiciatis unde omnis iste natus error sit voluptatem accusantium doloremque laudantium, totam rem aperiam, eaque ipsa quae ab illo inventore veritatis et quasi architecto beatae vitae dicta sunt explicabo. Nemo enim ipsam voluptatem quia voluptas sit aspernatur aut odit aut fugit, sed quia consequuntur magni dolores eos qui ratione voluptatem sequi nesciunt.<br><br>Laudantium, totam rem aperiam, eaque ipsa quae ab illo inventore veritatis et quasi architecto beatae vitae dicta sunt explicabo.</p>
  <div class="photo" role="img" aria-label="Collage of a laptop with charts and growing bar graph images" style="left:202px;top:213px;width:140px;height:115px;background:linear-gradient(135deg,#6d8fb8,#2c3e64 60%,#c9a87a)"></div>

  <div class="card" style="left:47px;top:344px;width:92px;height:66px;padding:10px 8px"><h4>Easy To Customize</h4><p class="body">Sed ut perspiciatis unde omnis iste voluptatem accusantium dummy doloremque laudantium.</p></div>
  <div class="card" style="left:148px;top:344px;width:92px;height:66px;padding:10px 8px"><h4>24/7 Support</h4><p class="body">Sed ut perspiciatis unde omnis iste voluptatem accusantium dummy doloremque laudantium.</p></div>
  <div class="card" style="left:249px;top:344px;width:92px;height:66px;padding:10px 8px"><h4>Advisory Team</h4><p class="body">Sed ut perspiciatis unde omnis iste voluptatem accusantium dummy doloremque laudantium.</p></div>

  <div class="heading" style="top:445px">Why Choose Us</div>
  <div style="position:absolute;left:150px;top:478px;width:88px;height:88px;border-radius:50%;background:var(--accent)"></div>
  <div style="position:absolute;left:43px;top:474px;width:80px;text-align:right"><h4 style="font-size:4.8px;font-weight:600">Cross Domain Support</h4><p class="body">Sed ut perspiciatis unde omnis iste voluptatem accusantium.</p></div>
  <div style="position:absolute;left:43px;top:511px;width:80px;text-align:right"><h4 style="font-size:4.8px;font-weight:600">Easy To Deploy</h4><p class="body">Sed ut perspiciatis unde omnis iste voluptatem accusantium.</p></div>
  <div style="position:absolute;left:43px;top:547px;width:80px;text-align:right"><h4 style="font-size:4.8px;font-weight:600">Real-Time Interaction</h4><p class="body">Sed ut perspiciatis unde omnis iste voluptatem accusantium.</p></div>
  <div style="position:absolute;left:264px;top:474px;width:80px"><h4 style="font-size:4.8px;font-weight:600">Error-Reduction</h4><p class="body">Sed ut perspiciatis unde omnis iste voluptatem accusantium.</p></div>
  <div style="position:absolute;left:264px;top:511px;width:80px"><h4 style="font-size:4.8px;font-weight:600">Quality &amp; Quantity Data</h4><p class="body">Sed ut perspiciatis unde omnis iste voluptatem accusantium.</p></div>
  <div style="position:absolute;left:264px;top:547px;width:80px"><h4 style="font-size:4.8px;font-weight:600">Research Process</h4><p class="body">Sed ut perspiciatis unde omnis iste voluptatem accusantium.</p></div>
  <svg style="position:absolute;left:126px;top:474px" width="12" height="90" aria-hidden="true"><g fill="none" stroke="var(--orange)" stroke-width=".8"><circle cx="6" cy="6" r="4.5"/><rect x="1.5" y="38" width="9" height="8"/><circle cx="6" cy="80" r="4.5"/></g></svg>
  <svg style="position:absolute;left:250px;top:474px" width="12" height="90" aria-hidden="true"><g fill="none" stroke="var(--accent)" stroke-width=".8"><circle cx="6" cy="6" r="4.5"/><circle cx="6" cy="42" r="4.5"/><rect x="1.5" y="76" width="9" height="8"/></g></svg>

  <footer class="footer" style="height:173px">
    <div class="footer-main">
      <div class="f-logo"><i></i>Metricsy Hub</div>
      <p class="f-desc">Sed ut perspiciatis unde omnis iste natus error sit voluptatem accusantium doloremque laudantium, totam rem aperiam, eaque ipsa quae ab illo inventore veritatis et quasi</p>
      <div class="f-social"><span></span><span></span><span></span><span></span></div>
      <div class="f-col-h" style="left:155px">CONTACT US</div>
      <div class="f-contact"><p><svg viewBox="0 0 10 10"><path d="M5 1a3 3 0 0 1 3 3c0 2-3 5-3 5S2 6 2 4a3 3 0 0 1 3-3z" fill="none" stroke="#fff" stroke-width=".8"/></svg>Metricsy Hub<br>250 ipsam voluptatem<br>quia voluptas</p><p><svg viewBox="0 0 10 10"><path d="M2 1l2 0 1 2-1 1a5 5 0 0 0 2 2l1-1 2 1v2c-4 0-7-3-7-7z" fill="none" stroke="#fff" stroke-width=".8"/></svg>Phone :<br>555-0142-7780</p><p><svg viewBox="0 0 10 10"><rect x="1" y="2.5" width="8" height="5.5" fill="none" stroke="#fff" stroke-width=".8"/><path d="M1 2.5l4 3 4-3" fill="none" stroke="#fff" stroke-width=".8"/></svg>Email :<br>info@metricsyhub.com</p></div>
      <div class="f-col-h" style="left:244px">SIGN UP TO RECEIVE EMAIL</div>
      <div class="f-sign">Excepteur sint occaecat cupidatat non proident, sunt in culpa qui officia deserunt mollit.<div class="f-input">Enter Email</div><span class="f-btn">SUBSCRIBE</span></div>
    </div>
    <div class="footer-bar">Copyright © Metricsy Hub 2021. All rights reserved. | Privacy Policy</div>
  </footer>
</section>

<!-- SERVICES -->
<h2 class="section-title" style="left:655px;top:684px">WHAT WE OFFER</h2>
<section class="page" style="left:655px;top:735px;height:775px">
  <nav class="nav"><div class="nav-logo"><i></i>Metricsy Hub</div><div class="nav-links"><span>Home</span><span>About us</span><span class="on">Our Service</span><span>Blog</span><span>Contact</span></div><div class="nav-cta">GET STARTED</div></nav>
  <div class="hero" role="img" aria-label="Hero photo of a hand holding a glowing holographic city"></div>
  <svg class="hero-edge" viewBox="0 0 388 132" aria-hidden="true"><polyline points="80,110 186,130 388,95" fill="none" stroke="var(--accent)" stroke-width="2"/></svg>
  <div class="hero-title">Our Services</div>
  <div class="crumb"><b></b>Home | Services</div>

  <div class="heading" style="top:183px">What We Offer</div>
  <div style="position:absolute;left:193px;top:222px;width:1px;height:372px;background:var(--line)"></div>

  <div class="dot" style="left:190px;top:222px"></div>
  <div style="position:absolute;left:46px;top:218px;width:112px"><h4 style="font-size:5px;font-weight:600">Neque porro quisquam</h4><p class="body">Aenean sollicitudin lorem quis auctor nisi elit consequat ipsum, nec sagittis sem nibh id elit. Duis sed odio sit amet nibh vulputate cursus.</p></div>
  <div class="icon-bubble" style="left:228px;top:223px"></div>
  <svg class="icon-box" style="left:230px;top:221px" viewBox="0 0 22 22" aria-hidden="true"><g fill="none" stroke="#2f2f3a" stroke-width=".9"><rect x="3" y="3" width="13" height="16"/><path d="M6 16v-3M9 16v-6M12 16v-4"/></g><circle cx="16" cy="6" r="3" fill="var(--orange)"/></svg>

  <div class="dot" style="left:190px;top:286px"></div>
  <div style="position:absolute;left:230px;top:282px;width:112px"><h4 style="font-size:5px;font-weight:600">Neque porro quisquam</h4><p class="body">Aenean sollicitudin lorem quis auctor nisi elit consequat ipsum, nec sagittis sem nibh id elit. Duis sed odio sit amet nibh vulputate cursus.</p></div>
  <div class="icon-bubble" style="left:116px;top:275px"></div>
  <svg class="icon-box" style="left:134px;top:273px" viewBox="0 0 22 22" aria-hidden="true"><g fill="none" stroke="#2f2f3a" stroke-width=".9"><circle cx="9" cy="9" r="6"/><path d="M13 13l6 6"/></g><circle cx="9" cy="9" r="2.5" fill="var(--accent)"/></svg>

  <div class="dot" style="left:190px;top:350px"></div>
  <div style="position:absolute;left:46px;top:346px;width:112px"><h4 style="font-size:5px;font-weight:600">Neque porro quisquam</h4><p class="body">Aenean sollicitudin lorem quis auctor nisi elit consequat ipsum, nec sagittis sem nibh id elit. Duis sed odio sit amet nibh vulputate cursus.</p></div>
  <div class="icon-bubble" style="left:228px;top:351px"></div>
  <svg class="icon-box" style="left:230px;top:349px" viewBox="0 0 22 22" aria-hidden="true"><g fill="none" stroke="#2f2f3a" stroke-width=".9"><rect x="2" y="4" width="15" height="11"/><path d="M5 12l3-3 3 2 4-4"/></g><circle cx="18" cy="16" r="3" fill="var(--orange)"/></svg>

  <div class="dot" style="left:190px;top:414px"></div>
  <div style="position:absolute;left:230px;top:410px;width:112px"><h4 style="font-size:5px;font-weight:600">Neque porro quisquam</h4><p class="body">Aenean sollicitudin lorem quis auctor nisi elit consequat ipsum, nec sagittis sem nibh id elit. Duis sed odio sit amet nibh vulputate cursus.</p></div>
  <div class="icon-bubble" style="left:116px;top:403px"></div>
  <svg class="icon-box" style="left:134px;top:401px" viewBox="0 0 22 22" aria-hidden="true"><g fill="none" stroke="#2f2f3a" stroke-width=".9"><rect x="2" y="5" width="14" height="11"/><path d="M16 10h4v8H8v-2"/></g><rect x="5" y="9" width="5" height="4" fill="var(--orange)"/></svg>

  <div class="dot" style="left:190px;top:478px"></div>
  <div style="position:absolute;left:46px;top:474px;width:112px"><h4 style="font-size:5px;font-weight:600">Neque porro quisquam</h4><p class="body">Aenean sollicitudin lorem quis auctor nisi elit consequat ipsum, nec sagittis sem nibh id elit. Duis sed odio sit amet nibh vulputate cursus.</p></div>
  <div class="icon-bubble" style="left:228px;top:479px"></div>
  <svg class="icon-box" style="left:230px;top:477px" viewBox="0 0 22 22" aria-hidden="true"><g fill="none" stroke="#2f2f3a" stroke-width=".9"><path d="M3 3v16h16"/><path d="M6 15l4-5 3 3 5-7"/></g><circle cx="16" cy="6" r="3" fill="var(--orange)"/></svg>

  <div class="dot" style="left:190px;top:542px"></div>
  <div style="position:absolute;left:230px;top:538px;width:112px"><h4 style="font-size:5px;font-weight:600">Neque porro quisquam</h4><p class="body">Aenean sollicitudin lorem quis auctor nisi elit consequat ipsum, nec sagittis sem nibh id elit. Duis sed odio sit amet nibh vulputate cursus.</p></div>
  <div class="icon-bubble" style="left:116px;top:531px"></div>
  <svg class="icon-box" style="left:134px;top:529px" viewBox="0 0 22 22" aria-hidden="true"><g fill="none" stroke="#2f2f3a" stroke-width=".9"><rect x="3" y="2" width="13" height="17"/><path d="M6 7h7M6 11h7M6 15h4"/></g><circle cx="17" cy="16" r="3.5" fill="none" stroke="var(--orange)" stroke-width="1"/></svg>

  <footer class="footer" style="height:173px">
    <div class="footer-main">
      <div class="f-logo"><i></i>Metricsy Hub</div>
      <p class="f-desc">Sed ut perspiciatis unde omnis iste natus error sit voluptatem accusantium doloremque laudantium, totam rem aperiam, eaque ipsa quae ab illo inventore veritatis et quasi</p>
      <div class="f-social"><span></span><span></span><span></span><span></span></div>
      <div class="f-col-h" style="left:155px">CONTACT US</div>
      <div class="f-contact"><p><svg viewBox="0 0 10 10"><path d="M5 1a3 3 0 0 1 3 3c0 2-3 5-3 5S2 6 2 4a3 3 0 0 1 3-3z" fill="none" stroke="#fff" stroke-width=".8"/></svg>Metricsy Hub<br>250 ipsam voluptatem<br>quia voluptas</p><p><svg viewBox="0 0 10 10"><path d="M2 1l2 0 1 2-1 1a5 5 0 0 0 2 2l1-1 2 1v2c-4 0-7-3-7-7z" fill="none" stroke="#fff" stroke-width=".8"/></svg>Phone :<br>555-0142-7780</p><p><svg viewBox="0 0 10 10"><rect x="1" y="2.5" width="8" height="5.5" fill="none" stroke="#fff" stroke-width=".8"/><path d="M1 2.5l4 3 4-3" fill="none" stroke="#fff" stroke-width=".8"/></svg>Email :<br>info@metricsyhub.com</p></div>
      <div class="f-col-h" style="left:244px">SIGN UP TO RECEIVE EMAIL</div>
      <div class="f-sign">Excepteur sint occaecat cupidatat non proident, sunt in culpa qui officia deserunt mollit.<div class="f-input">Enter Email</div><span class="f-btn">SUBSCRIBE</span></div>
    </div>
    <div class="footer-bar">Copyright © Metricsy Hub 2021. All rights reserved. | Privacy Policy</div>
  </footer>
</section>

<!-- TESTIMONIALS -->
<h2 class="section-title" style="left:196px;top:1206px">TESTIMONIALS</h2>
<section class="page" style="left:197px;top:1255px;height:754px">
  <nav class="nav"><div class="nav-logo"><i></i>Metricsy Hub</div><div class="nav-links"><span>Home</span><span>About us</span><span>Our Service</span><span>Blog</span><span>Contact</span></div><div class="nav-cta">GET STARTED</div></nav>
  <div class="hero" role="img" aria-label="Hero photo of two colleagues reviewing work on a laptop"></div>
  <svg class="hero-edge" viewBox="0 0 388 132" aria-hidden="true"><polyline points="80,110 186,130 388,95" fill="none" stroke="var(--accent)" stroke-width="2"/></svg>
  <div class="hero-title">Testimonials</div>
  <div class="crumb"><b></b>Home | Testimonials</div>

  <div class="heading" style="top:186px">Customer Reviews and Use Cases</div>

  <div class="card" style="left:47px;top:236px;width:92px;height:58px;padding:10px 8px;text-align:center"><p class="body">Proin gravida nibh vel velit auctor aliquet. Aenean sollicitudin lorem quis bibendum auctor, nisi elit.</p><div class="stars">★★★★★</div></div>
  <div class="card" style="left:148px;top:236px;width:92px;height:58px;padding:10px 8px;text-align:center"><p class="body">Proin gravida nibh vel velit auctor aliquet. Aenean sollicitudin lorem quis bibendum auctor, nisi elit.</p><div class="stars">★★★★★</div></div>
  <div class="card" style="left:249px;top:236px;width:92px;height:58px;padding:10px 8px;text-align:center"><p class="body">Proin gravida nibh vel velit auctor aliquet. Aenean sollicitudin lorem quis bibendum auctor, nisi elit.</p><div class="stars">★★★★★</div></div>
  <div class="person" style="left:52px;top:300px"><span class="avatar"></span><div>Mark T.<small>Metricsy Hub</small></div></div>
  <div class="person" style="left:153px;top:300px"><span class="avatar"></span><div>Nina P.<small>Metricsy Hub</small></div></div>
  <div class="person" style="left:254px;top:300px"><span class="avatar"></span><div>Owen K.<small>Metricsy Hub</small></div></div>

  <div class="card" style="left:47px;top:333px;width:92px;height:58px;padding:10px 8px;text-align:center"><p class="body">Proin gravida nibh vel velit auctor aliquet. Aenean sollicitudin lorem quis bibendum auctor, nisi elit.</p><div class="stars">★★★★★</div></div>
  <div class="card" style="left:148px;top:333px;width:92px;height:58px;padding:10px 8px;text-align:center"><p class="body">Proin gravida nibh vel velit auctor aliquet. Aenean sollicitudin lorem quis bibendum auctor, nisi elit.</p><div class="stars">★★★★★</div></div>
  <div class="card" style="left:249px;top:333px;width:92px;height:58px;padding:10px 8px;text-align:center"><p class="body">Proin gravida nibh vel velit auctor aliquet. Aenean sollicitudin lorem quis bibendum auctor, nisi elit.</p><div class="stars">★★★★★</div></div>
  <div class="person" style="left:52px;top:397px"><span class="avatar"></span><div>Mark T.<small>Metricsy Hub</small></div></div>
  <div class="person" style="left:153px;top:397px"><span class="avatar"></span><div>Nina P.<small>Metricsy Hub</small></div></div>
  <div class="person" style="left:254px;top:397px"><span class="avatar"></span><div>Owen K.<small>Metricsy Hub</small></div></div>

  <div class="card" style="left:47px;top:430px;width:92px;height:58px;padding:10px 8px;text-align:center"><p class="body">Proin gravida nibh vel velit auctor aliquet. Aenean sollicitudin lorem quis bibendum auctor, nisi elit.</p><div class="stars">★★★★★</div></div>
  <div class="card" style="left:148px;top:430px;width:92px;height:58px;padding:10px 8px;text-align:center"><p class="body">Proin gravida nibh vel velit auctor aliquet. Aenean sollicitudin lorem quis bibendum auctor, nisi elit.</p><div class="stars">★★★★★</div></div>
  <div class="card" style="left:249px;top:430px;width:92px;height:58px;padding:10px 8px;text-align:center"><p class="body">Proin gravida nibh vel velit auctor aliquet. Aenean sollicitudin lorem quis bibendum auctor, nisi elit.</p><div class="stars">★★★★★</div></div>
  <div class="person" style="left:52px;top:494px"><span class="avatar"></span><div>Mark T.<small>Metricsy Hub</small></div></div>
  <div class="person" style="left:153px;top:494px"><span class="avatar"></span><div>Nina P.<small>Metricsy Hub</small></div></div>
  <div class="person" style="left:254px;top:494px"><span class="avatar"></span><div>Owen K.<small>Metricsy Hub</small></div></div>

  <div style="position:absolute;left:173px;top:529px;background:var(--orange);color:#fff;font-size:4px;font-weight:600;padding:3px 7px">LOAD MORE</div>

  <footer class="footer" style="height:173px">
    <div class="footer-main">
      <div class="f-logo"><i></i>Metricsy Hub</div>
      <p class="f-desc">Sed ut perspiciatis unde omnis iste natus error sit voluptatem accusantium doloremque laudantium, totam rem aperiam, eaque ipsa quae ab illo inventore veritatis et quasi</p>
      <div class="f-social"><span></span><span></span><span></span><span></span></div>
      <div class="f-col-h" style="left:155px">CONTACT US</div>
      <div class="f-contact"><p><svg viewBox="0 0 10 10"><path d="M5 1a3 3 0 0 1 3 3c0 2-3 5-3 5S2 6 2 4a3 3 0 0 1 3-3z" fill="none" stroke="#fff" stroke-width=".8"/></svg>Metricsy Hub<br>250 ipsam voluptatem<br>quia voluptas</p><p><svg viewBox="0 0 10 10"><path d="M2 1l2 0 1 2-1 1a5 5 0 0 0 2 2l1-1 2 1v2c-4 0-7-3-7-7z" fill="none" stroke="#fff" stroke-width=".8"/></svg>Phone :<br>555-0142-7780</p><p><svg viewBox="0 0 10 10"><rect x="1" y="2.5" width="8" height="5.5" fill="none" stroke="#fff" stroke-width=".8"/><path d="M1 2.5l4 3 4-3" fill="none" stroke="#fff" stroke-width=".8"/></svg>Email :<br>info@metricsyhub.com</p></div>
      <div class="f-col-h" style="left:244px">SIGN UP TO RECEIVE EMAIL</div>
      <div class="f-sign">Excepteur sint occaecat cupidatat non proident, sunt in culpa qui officia deserunt mollit.<div class="f-input">Enter Email</div><span class="f-btn">SUBSCRIBE</span></div>
    </div>
    <div class="footer-bar">Copyright © Metricsy Hub 2021. All rights reserved. | Privacy Policy</div>
  </footer>
</section>

<!-- BLOG -->
<h2 class="section-title" style="left:644px;top:1581px">LATEST BLOG</h2>
<section class="page" style="left:644px;top:1630px;height:841px">
  <nav class="nav"><div class="nav-logo"><i></i>Metricsy Hub</div><div class="nav-links"><span>Home</span><span>About us</span><span>Our Service</span><span class="on">Blog</span><span>Contact</span></div><div class="nav-cta">GET STARTED</div></nav>
  <div class="hero" role="img" aria-label="Hero photo of a businessman touching floating chart graphics"></div>
  <svg class="hero-edge" viewBox="0 0 388 132" aria-hidden="true"><polyline points="80,110 186,130 388,95" fill="none" stroke="var(--accent)" stroke-width="2"/></svg>
  <div class="hero-title">Latest Blog</div>
  <div class="crumb"><b></b>Home | Blog</div>

  <div class="card" style="left:46px;top:187px;width:108px;height:136px"><div class="photo" role="img" aria-label="Blog photo of printed reports on a desk" style="left:0;top:0;width:108px;height:70px;background:linear-gradient(135deg,#c8c5c0,#6b6a70)"></div><div style="position:absolute;left:6px;top:76px;width:96px"><div style="font-size:3.4px;color:var(--muted)">26-02-2021</div><h4 style="font-size:5px;margin:2px 0">Sem nibh id elit duis sed odio sit amet vulputat...</h4><p class="body" style="font-size:3.8px">Aenean sollicitudin lorem quis auctor nisi elit consequat ipsum, nec sagittis sem nibh.</p><div style="color:var(--orange);font-size:5px">→</div></div></div>
  <div class="card" style="left:160px;top:187px;width:108px;height:136px"><div class="photo" role="img" aria-label="Blog photo of a hand with a rising chart" style="left:0;top:0;width:108px;height:70px;background:linear-gradient(135deg,#2a5a8e,#0f2545)"></div><div style="position:absolute;left:6px;top:76px;width:96px"><div style="font-size:3.4px;color:var(--muted)">26-02-2021</div><h4 style="font-size:5px;margin:2px 0">Sem nibh id elit duis sed odio sit amet vulputat...</h4><p class="body" style="font-size:3.8px">Aenean sollicitudin lorem quis auctor nisi elit consequat ipsum, nec sagittis sem nibh.</p><div style="color:var(--orange);font-size:5px">→</div></div></div>
  <div class="card" style="left:46px;top:332px;width:108px;height:136px"><div class="photo" role="img" aria-label="Blog photo of a glowing 3D bar chart" style="left:0;top:0;width:108px;height:70px;background:linear-gradient(135deg,#0c1f4a,#2f6fb8)"></div><div style="position:absolute;left:6px;top:76px;width:96px"><div style="font-size:3.4px;color:var(--muted)">26-02-2021</div><h4 style="font-size:5px;margin:2px 0">Sem nibh id elit duis sed odio sit amet vulputat...</h4><p class="body" style="font-size:3.8px">Aenean sollicitudin lorem quis auctor nisi elit consequat ipsum, nec sagittis sem nibh.</p><div style="color:var(--orange);font-size:5px">→</div></div></div>
  <div class="card" style="left:160px;top:332px;width:108px;height:136px"><div class="photo" role="img" aria-label="Blog photo of a laptop with charts on screen" style="left:0;top:0;width:108px;height:70px;background:linear-gradient(135deg,#9a8f86,#3d3a40)"></div><div style="position:absolute;left:6px;top:76px;width:96px"><div style="font-size:3.4px;color:var(--muted)">26-02-2021</div><h4 style="font-size:5px;margin:2px 0">Sem nibh id elit duis sed odio sit amet vulputat...</h4><p class="body" style="font-size:3.8px">Aenean sollicitudin lorem quis auctor nisi elit consequat ipsum, nec sagittis sem nibh.</p><div style="color:var(--orange);font-size:5px">→</div></div></div>
  <div class="card" style="left:46px;top:477px;width:108px;height:136px"><div class="photo" role="img" aria-label="Blog photo of a digital data dashboard" style="left:0;top:0;width:108px;height:70px;background:linear-gradient(135deg,#1b4e86,#5aa0d8)"></div><div style="position:absolute;left:6px;top:76px;width:96px"><div style="font-size:3.4px;color:var(--muted)">26-02-2021</div><h4 style="font-size:5px;margin:2px 0">Sem nibh id elit duis sed odio sit amet vulputat...</h4><p class="body" style="font-size:3.8px">Aenean sollicitudin lorem quis auctor nisi elit consequat ipsum, nec sagittis sem nibh.</p><div style="color:var(--orange);font-size:5px">→</div></div></div>
  <div class="card" style="left:160px;top:477px;width:108px;height:136px"><div class="photo" role="img" aria-label="Blog photo of an analyst at a monitor" style="left:0;top:0;width:108px;height:70px;background:linear-gradient(135deg,#6f7d92,#28344a)"></div><div style="position:absolute;left:6px;top:76px;width:96px"><div style="font-size:3.4px;color:var(--muted)">26-02-2021</div><h4 style="font-size:5px;margin:2px 0">Sem nibh id elit duis sed odio sit amet vulputat...</h4><p class="body" style="font-size:3.8px">Aenean sollicitudin lorem quis auctor nisi elit consequat ipsum, nec sagittis sem nibh.</p><div style="color:var(--orange);font-size:5px">→</div></div></div>

  <aside style="position:absolute;left:281px;top:187px;width:64px;font-size:4px">
    <div style="font-weight:600;font-size:4.4px">Search</div>
    <div style="margin-top:3px;height:9px;border:.6px solid var(--line);font-size:3.4px;color:var(--muted);padding:2px 3px">Search our blog</div>
    <div style="font-weight:600;font-size:4.4px;margin-top:9px">Categories</div>
    <div class="body" style="font-size:3.6px;line-height:2.2">View all<br>Business Continuity<br>Disaster Recovery<br>Pandemic<br>More</div>
    <div style="font-weight:600;font-size:4.4px;margin-top:10px">Recent Articles</div>
    <div style="display:flex;gap:3px;margin-top:5px"><span style="width:22px;height:18px;background:linear-gradient(135deg,#2a5a8e,#8fb3d8)" role="img" aria-label="Article thumbnail"></span><div style="font-size:3.3px;line-height:1.4"><span style="color:var(--muted)">26-02-2021</span><br><b style="font-weight:600">Why the Internet<br>is an Elephant</b></div></div>
    <div style="display:flex;gap:3px;margin-top:8px"><span style="width:22px;height:18px;background:linear-gradient(135deg,#c49a62,#5a4030)" role="img" aria-label="Article thumbnail"></span><div style="font-size:3.3px;line-height:1.4"><span style="color:var(--muted)">26-02-2021</span><br><b style="font-weight:600">8 Ways to Bring<br>Nature Indoors</b></div></div>
    <div style="display:flex;gap:3px;margin-top:8px"><span style="width:22px;height:18px;background:linear-gradient(135deg,#d8c9b0,#7c6a55)" role="img" aria-label="Article thumbnail"></span><div style="font-size:3.3px;line-height:1.4"><span style="color:var(--muted)">26-02-2021</span><br><b style="font-weight:600">Are You a<br>Minimalist?</b></div></div>
    <div style="display:flex;gap:3px;margin-top:8px"><span style="width:22px;height:18px;background:linear-gradient(135deg,#9aa6b4,#3c4654)" role="img" aria-label="Article thumbnail"></span><div style="font-size:3.3px;line-height:1.4"><span style="color:var(--muted)">26-02-2021</span><br><b style="font-weight:600">6 Ways to Bring<br>Nature Indoors</b></div></div>
  </aside>

  <div style="position:absolute;left:46px;top:626px;display:flex;gap:6px;font-size:4px;color:var(--muted);align-items:center"><span>‹</span><span>1</span><span>2</span><span style="width:9px;height:9px;border-radius:50%;background:var(--footer);color:#fff;text-align:center;line-height:9px">3</span><span>4</span><span>5</span><span>›</span></div>

  <footer class="footer" style="height:173px">
    <div class="footer-main">
      <div class="f-logo"><i></i>Metricsy Hub</div>
      <p class="f-desc">Sed ut perspiciatis unde omnis iste natus error sit voluptatem accusantium doloremque laudantium, totam rem aperiam, eaque ipsa quae ab illo inventore veritatis et quasi</p>
      <div class="f-social"><span></span><span></span><span></span><span></span></div>
      <div class="f-col-h" style="left:155px">CONTACT US</div>
      <div class="f-contact"><p><svg viewBox="0 0 10 10"><path d="M5 1a3 3 0 0 1 3 3c0 2-3 5-3 5S2 6 2 4a3 3 0 0 1 3-3z" fill="none" stroke="#fff" stroke-width=".8"/></svg>Metricsy Hub<br>250 ipsam voluptatem<br>quia voluptas</p><p><svg viewBox="0 0 10 10"><path d="M2 1l2 0 1 2-1 1a5 5 0 0 0 2 2l1-1 2 1v2c-4 0-7-3-7-7z" fill="none" stroke="#fff" stroke-width=".8"/></svg>Phone :<br>555-0142-7780</p><p><svg viewBox="0 0 10 10"><rect x="1" y="2.5" width="8" height="5.5" fill="none" stroke="#fff" stroke-width=".8"/><path d="M1 2.5l4 3 4-3" fill="none" stroke="#fff" stroke-width=".8"/></svg>Email :<br>info@metricsyhub.com</p></div>
      <div class="f-col-h" style="left:244px">SIGN UP TO RECEIVE EMAIL</div>
      <div class="f-sign">Excepteur sint occaecat cupidatat non proident, sunt in culpa qui officia deserunt mollit.<div class="f-input">Enter Email</div><span class="f-btn">SUBSCRIBE</span></div>
    </div>
    <div class="footer-bar">Copyright © Metricsy Hub 2021. All rights reserved. | Privacy Policy</div>
  </footer>
</section>

<!-- CONTACT -->
<h2 class="section-title" style="left:196px;top:2069px">CONTACT US</h2>
<section class="page" style="left:197px;top:2115px;height:710px">
  <nav class="nav"><div class="nav-logo"><i></i>Metricsy Hub</div><div class="nav-links"><span>Home</span><span>About us</span><span>Our Service</span><span>Blog</span><span class="on">Contact</span></div><div class="nav-cta">GET STARTED</div></nav>
  <div class="hero" role="img" aria-label="Hero photo of a hand holding a smartphone with floating icons"></div>
  <svg class="hero-edge" viewBox="0 0 388 132" aria-hidden="true"><polyline points="80,110 186,130 388,95" fill="none" stroke="var(--accent)" stroke-width="2"/></svg>
  <div class="hero-title">Contact Us</div>
  <div class="crumb"><b></b>Home | Contact</div>

  <div style="position:absolute;left:69px;top:196px;font-size:10px">Get In Touch</div>
  <div style="position:absolute;left:69px;top:218px;font-size:4.2px;line-height:1.45;width:100px">
    <p style="margin-bottom:6px"><b style="font-weight:600">● Location</b><br>Metricsy Hub 250 ipsam voluptatem quia voluptas</p>
    <p style="margin-bottom:6px"><b style="font-weight:600">● Phone</b><br>Call Us: 555-0142-7780</p>
    <p style="margin-bottom:6px"><b style="font-weight:600">● Email</b><br>info@metricsyhub.com</p>
    <p style="margin-bottom:6px"><b style="font-weight:600">● Opening Hours</b><br>Monday - Sunday: 8:30 AM - 6:00 PM</p>
    <div style="display:flex;gap:3px;margin-top:4px"><span style="width:8px;height:8px;border-radius:50%;background:#3b5cc4"></span><span style="width:8px;height:8px;border-radius:50%;background:#3aa3e8"></span><span style="width:8px;height:8px;border-radius:50%;background:#e04a3a"></span><span style="width:8px;height:8px;border-radius:50%;background:#c23a9a"></span><span style="width:8px;height:8px;border-radius:50%;background:#d9232a"></span></div>
  </div>

  <div style="position:absolute;left:192px;top:185px;width:113px;height:180px;background:var(--accent);padding:10px 12px;color:#fff">
    <div style="font-size:8.5px">Get A Free Quote</div>
    <div style="font-size:3.2px;margin-top:6px">YOUR NAME*</div><div style="height:10px;background:#fff;color:var(--muted);font-size:3.6px;padding:3px">Enter name</div>
    <div style="font-size:3.2px;margin-top:5px">PHONE NUMBER</div><div style="height:10px;background:#fff;color:var(--muted);font-size:3.6px;padding:3px">Enter Phone number</div>
    <div style="font-size:3.2px;margin-top:5px">E-MAIL*</div><div style="height:10px;background:#fff;color:var(--muted);font-size:3.6px;padding:3px">Enter email address</div>
    <div style="font-size:3.2px;margin-top:5px">COUNTRY*</div><div style="height:10px;background:#fff;color:var(--muted);font-size:3.6px;padding:3px;display:flex;justify-content:space-between"><span>Choose your country</span><span>▾</span></div>
    <div style="margin:10px auto 0;width:44px;background:var(--orange);font-size:3.8px;font-weight:600;text-align:center;padding:3px 0">GET STARTED</div>
  </div>

  <div class="card" style="left:46px;top:370px;width:296px;height:110px">
    <div role="img" aria-label="Street map showing the office location" style="position:absolute;inset:0;background:linear-gradient(135deg,#eeeeee,#dcdcdc)"></div>
    <svg style="position:absolute;left:138px;top:28px" width="10" height="13" viewBox="0 0 10 13" aria-hidden="true"><path d="M5 0a5 5 0 0 1 5 5c0 3-5 8-5 8S0 8 0 5a5 5 0 0 1 5-5z" fill="#222"/><circle cx="5" cy="5" r="2" fill="#fff"/></svg>
    <div style="position:absolute;left:108px;top:60px;width:72px;height:26px;border-radius:13px;background:#fff;font-size:3.6px;text-align:center;padding-top:5px;line-height:1.4"><b style="font-weight:600">Location</b><br>Metricsy Hub 250 ipsam<br>voluptatem quia voluptas</div>
  </div>

  <footer class="footer" style="height:181px">
    <div class="footer-main" style="height:135px">
      <div class="f-logo"><i></i>Metricsy Hub</div>
      <p class="f-desc">Sed ut perspiciatis unde omnis iste natus error sit voluptatem accusantium doloremque laudantium, totam rem aperiam, eaque ipsa quae ab illo inventore veritatis et quasi</p>
      <div class="f-social"><span></span><span></span><span></span><span></span></div>
      <div class="f-col-h" style="left:155px">CONTACT US</div>
      <div class="f-contact"><p><svg viewBox="0 0 10 10"><path d="M5 1a3 3 0 0 1 3 3c0 2-3 5-3 5S2 6 2 4a3 3 0 0 1 3-3z" fill="none" stroke="#fff" stroke-width=".8"/></svg>Metricsy Hub<br>250 ipsam voluptatem<br>quia voluptas</p><p><svg viewBox="0 0 10 10"><path d="M2 1l2 0 1 2-1 1a5 5 0 0 0 2 2l1-1 2 1v2c-4 0-7-3-7-7z" fill="none" stroke="#fff" stroke-width=".8"/></svg>Phone :<br>555-0142-7780</p><p><svg viewBox="0 0 10 10"><rect x="1" y="2.5" width="8" height="5.5" fill="none" stroke="#fff" stroke-width=".8"/><path d="M1 2.5l4 3 4-3" fill="none" stroke="#fff" stroke-width=".8"/></svg>Email :<br>info@metricsyhub.com</p></div>
      <div class="f-col-h" style="left:244px">SIGN UP TO RECEIVE EMAIL</div>
      <div class="f-sign">Excepteur sint occaecat cupidatat non proident, sunt in culpa qui officia deserunt mollit.<div class="f-input">Enter Email</div><span class="f-btn">SUBSCRIBE</span></div>
    </div>
    <div class="footer-bar">Copyright © Metricsy Hub 2021. All rights reserved. | Privacy Policy</div>
  </footer>
</section>

</body>
</html>
```